No Credit Score QT and ZMR

I'm looking for a banner to display on emails as well as facebook. The facebook banner would need to be square and the other size is 728 x 90. We are a mortgage company that does mostly Military home loans. We would like to start out with just this banner, then do about 20 others once we find the right designer. I need something simple but that stands out. Our company website is www.harborpeakfinancial.com. The text for this will be ( Ask about our "No Credit Score" program for ZMR and QT)

```html
<!DOCTYPE html>
<html lang="en">
<head>
<meta charset="utf-8">
<title>Harbor Peak Financial – No Credit Score Banner</title>
<link rel="stylesheet" href="https://fonts.googleapis.com/css2?family=Lato:wght@300;400;700;900&display=swap">
<style>
  :root {
    --page-bg: #f7f7f7;
    --banner-green: #6c922c;
    --chevron-light: rgba(255, 255, 255, 0.08);
    --text-light: #ffffff;
    --logo-ink: #262626;
    --flag-red: #c8283a;
    --flag-white: #f1eeee;
    --flag-blue: #2f4a8a;
    --house-grey: #b9bec6;
    --house-white: #eceef1;
  }
  html, body {
    margin: 0;
    padding: 0;
    width: 1200px;
    height: 1200px;
    overflow: hidden;
    background: var(--page-bg);
  }
  .canvas {
    position: relative;
    width: 1200px;
    height: 1200px;
  }
  .banner {
    position: absolute;
    left: 145px;
    top: 545px;
    width: 910px;
    height: 112.5px;
    overflow: hidden;
    background: var(--banner-green);
    box-shadow: 0 4px 14px rgba(0, 0, 0, 0.12);
  }
  .banner-art {
    position: absolute;
    inset: 0;
    width: 100%;
    height: 100%;
    display: block;
  }
  .brand-name {
    position: absolute;
    left: 20px;
    top: 44px;
    margin: 0;
    font-family: "Lato", sans-serif;
    font-weight: 700;
    font-size: 20px;
    letter-spacing: 2px;
    text-transform: uppercase;
    color: var(--logo-ink);
    line-height: 1;
  }
  .offer {
    position: absolute;
    left: 494px;
    right: 0;
    top: 24px;
    margin: 0;
    text-align: center;
    font-family: "Lato", sans-serif;
    font-weight: 300;
    font-size: 21px;
    line-height: 31px;
    color: var(--text-light);
  }
  .offer strong {
    font-weight: 900;
    letter-spacing: -0.3px;
  }
</style>
</head>
<body>
  <main class="canvas">
    <section class="banner">
      <svg class="banner-art" viewBox="0 0 728 90" preserveAspectRatio="none" aria-hidden="false">
        <defs>
          <linearGradient id="photo-tones" x1="0" y1="0" x2="1" y2="0.3">
            <stop offset="0" stop-color="var(--flag-red)"/>
            <stop offset="0.12" stop-color="var(--flag-white)"/>
            <stop offset="0.22" stop-color="var(--flag-blue)"/>
            <stop offset="0.38" stop-color="var(--flag-red)"/>
            <stop offset="0.55" stop-color="var(--flag-white)"/>
            <stop offset="0.72" stop-color="var(--house-white)"/>
            <stop offset="1" stop-color="var(--house-grey)"/>
          </linearGradient>
        </defs>
        <rect class="green-field" x="0" y="0" width="728" height="90" fill="var(--banner-green)"/>
        <polygon class="chevron-accent" points="370,0 392,0 407,45 392,90 370,90 385,45" fill="var(--chevron-light)"/>
        <polygon class="chevron-accent" points="470,0 488,0 503,45 488,90 470,90 485,45" fill="var(--chevron-light)"/>
        <polygon class="photo-area" role="img"
                 aria-label="Photo of American flags waving in front of a white house"
                 points="0,0 362,0 365,45 332,90 0,90"
                 fill="url(#photo-tones)"/>
      </svg>
      <p class="brand-name">Harbor Peak Financial</p>
      <p class="offer">Ask about our <strong>"No Credit Score"</strong><br>program for <strong>ZMR</strong> and <strong>QT</strong></p>
    </section>
  </main>
</body>
</html>
```